Steadfast Valve Works

I need a business card with the attached logo.
The second page I have attached is what we are looking for. We want doubles sided. We would like the blues fading and the logo on the back.

Industry/Entity Type

Business

```html
<!DOCTYPE html>
<html lang="en">
<head>
<meta charset="utf-8">
<title>Steadfast Valve Works – Business Card</title>
<link rel="stylesheet" href="https://fonts.googleapis.com/css2?family=Oswald:wght@300;500;600&display=swap">
<style>
  :root {
    --page-bg: #e6e6e6;
    --blue-edge: #58a6f4;
    --blue-mid: #9ccbf8;
    --blue-light: #7bbcf9;
    --card-white: #ffffff;
    --brand-blue: #1446c8;
    --text-white: #ffffff;
    --rule: rgba(255, 255, 255, 0.75);
  }
  html, body {
    margin: 0;
    padding: 0;
    width: 1200px;
    height: 1000px;
    overflow: hidden;
    background: var(--page-bg);
    font-family: "Oswald", sans-serif;
  }
  .canvas {
    position: relative;
    width: 1200px;
    height: 1000px;
  }
  .card {
    position: absolute;
    left: 342px;
    width: 516px;
    height: 324px;
    overflow: hidden;
  }
  .card--front {
    top: 114px;
    background: radial-gradient(ellipse 62% 62% at 50% 50%, var(--card-white) 0%, #e3f0fd 30%, var(--blue-mid) 62%, var(--blue-edge) 100%);
  }
  .card--back {
    top: 545px;
    background: linear-gradient(90deg, var(--blue-light) 0%, #a6d3fb 45%, #d6ebfd 72%, var(--card-white) 100%);
  }
  .brand-name {
    position: absolute;
    display: flex;
    align-items: center;
    gap: 8px;
    color: var(--brand-blue);
    font-weight: 600;
    text-transform: uppercase;
    white-space: nowrap;
  }
  .brand-name__mark {
    background: var(--brand-blue);
    flex: none;
  }
  .card--front .brand-name {
    left: 0;
    right: 0;
    top: 138px;
    justify-content: center;
    font-size: 34px;
    letter-spacing: 1px;
    line-height: 1;
  }
  .card--front .brand-name__mark { width: 22px; height: 22px; }
  .card--back .brand-name {
    right: 22px;
    top: 270px;
    font-size: 17px;
    letter-spacing: 0.5px;
    line-height: 1;
  }
  .card--back .brand-name__mark { width: 12px; height: 12px; }
  .contact {
    position: absolute;
    left: 20px;
    top: 146px;
    color: var(--text-white);
  }
  .contact__name {
    margin: 0;
    font-size: 34px;
    font-weight: 500;
    line-height: 1.05;
    text-transform: uppercase;
  }
  .contact__role {
    margin: 0;
    font-size: 19px;
    font-weight: 300;
    line-height: 1.2;
    text-transform: uppercase;
  }
  .contact__rule {
    width: 260px;
    height: 1px;
    margin: 6px 0 8px;
    background: var(--rule);
    border: 0;
  }
  .contact__line {
    margin: 0;
    font-size: 18px;
    font-weight: 300;
    line-height: 28px;
  }
  .contact__web {
    margin: 10px 0 0;
    font-size: 14px;
    font-weight: 300;
  }
</style>
</head>
<body>
<main class="canvas">
  <section class="card card--front" aria-label="Card front">
    <div class="brand-name">
      <span class="brand-name__mark"></span>
      <span>Steadfast Valve Works</span>
    </div>
  </section>

  <section class="card card--back" aria-label="Card back">
    <div class="contact">
      <h1 class="contact__name">Daniel Reyes</h1>
      <p class="contact__role">Regional Manager</p>
      <hr class="contact__rule">
      <p class="contact__line">Ph: +1 (0) 555 214 630</p>
      <p class="contact__line">E: info@steadfastvalve.com</p>
      <p class="contact__web">www.steadfastvalve.com</p>
    </div>
    <div class="brand-name">
      <span class="brand-name__mark"></span>
      <span>Steadfast Valve Works</span>
    </div>
  </section>
</main>
</body>
</html>
```